Our business name is Brightmoor Pty Ltd and we already have a logo. We would like the same colours that appear in our logo on our marketing material. I have attached our logo for colour consistency. We need a brochure designed that promotes our aerial photography and aerial imaging services. We'd like to use the brochure for electronic marketing purposes in an effort to attract a new client base. We are a new start up business so funds are fairly scarce. We use sophisticated UAV (unmanned aerial vehicle) or RPA - remotely piloted aircraft technology) that captures beautiful video and still images.
Our services are suitable for many types of industries and applications. We have identified at least 10 market sectors ranging, infrastructure inspections such as: gas pipelines, chemical and petrol storage facilities, pipeline and power line inspections, Archeological and geological surveys, vegetation mapping, wildlife surveys, agriculture and horticulture surveys, high end real estate, sport and event marketing. Our plan is to create a series of brochures (1) for each industry to help us market our business.

Our first brochure will focus on environmental management and compliance. We will target other industries down the track. These industries would see our service as helping them meet their compliance and auditing requirements.
We have a brochure that we put together containing words and some (very boring) format. As this will be one of a series of brochures, we'd like to colour code the industries for easy identification. (perhaps a green tab) in the corner to distinguish between our brochures. We have attached our boring brochure as a starting point. If we like the design there will be more work to follow. We want to be able to standardise the format for the other industries we will target. We anticipate needing another 6-8 brochures over the course of the next 2 months.

I have received questions regarding brochure size.  Apologies, I should have indicated in my posting previously.  The brochure is A3 landscape size so it can be folded in half to make 4 A4 pages.  We need to keep printing costs down so the content needs to be  within 4 pages.  I'm about to make some minor changes to the content to try to reduce the amount of text cause I can see this may be a problem.  Look forward to receiving your design. Thanking you in advance for your great work!

Re: Brochure Brightmoor Environmental Compliance and Monitoring Services

I have reduced the amount of text contained in the original version of the brochure making it more succinct and less wordy.  Could you use the least amount of space because we want to be able to use this brochure as both electric marketing and print based.  I have also included additional photos which will give you more to work with.  Thank you for your work in advance!  Regards Marta 

PLEASE NOTE - TEXT HAS BEEN UPDATED (REDUCED TEXT IN BROCHURE). COULD YOU REFER TO VERSION 2 OF BRIGHTMOOR ENVIRONMENTAL COMPLIANCE AND MONITORING SERVICES BROCHURE UPDATED FRIDAY 17TH.

Thanks Marta 

Hi talented designers working on the Brightmoor Brochure for Environmental Compliance and Monitoring.  I have been asked to upload the EPS version of Brightmoor Logo.  I have just done so.

Regards
Marta 

Hi all, to assist you with the design concept. I feel I need to clarity a number of points.  We are a new technology driven business.  No one else is conducting environmental surveys using this type of sophisticated equipment. We are in the business of providing clients with visual data (aerial images). Could you include grab lines in the brochure that draws attention to this. We us state of the art technology to produce high quality images efficiently, safely and economically. 

Thank you
Marta

Reason: We need additional time to receive and review designs.

Reason: Need additional time to communicate with designers and to review changes. Thank you Marta

I have extended the project date a few days. I have been incredibly impressed by the quality of your work and thank you all for your efforts.  I am waiting on a few revisions by a number of designers and look forward to receiving these changes.  We are close to completion.  Thanking you all again. Marta 

We are targeting a wide range of industry sectors. Specifically, looking at targeting large engineering type consultancies, corporations, government agencies, auditing bodies. Typically, targeting the professional sector who use data to confirm, monitor and make better decisions.

We want the brochure design to be contemporary and modern which reflects what our business does. We use state of the art unmanned aerial technology to capture brilliant visual images and video. So we want our brochure to reflect that we're leaders in the field offering something different - cutting edge approach. I have additional photos that show vegetation mapping, wildlife surveys, agriculture and horticulture applications. Our services would benefit any business that uses visual data to help them make better, more informed decisions.

Business

Serif
Sans Serif

• We would like you to include photo of the UAV equipment/technology shots. This is new technology so we must also educate our clients on what our technology is capable of doing. We are offering a service that is very different so we want to be able to convey the true benefits of our services such as safety, efficiency, cost saving, reliability. We would like to convey these key themes. Credible data enables businesses to make better, faster decisions.
• We are essentially providing visual data in the form of high definition photos and videos. For this particular sector, data could be used for compliance or auditing purposes, planning, measuring, monitoring, evaluating, assessing, marketing. Could you please include these words in the brochure as they capture our service provision. Please note the red photo is infrared images.

```html
<!DOCTYPE html>
<html lang="en">
<head>
<meta charset="utf-8">
<title>Brightmoor – Environmental Compliance And Monitoring Services</title>
<link rel="stylesheet" href="https://fonts.googleapis.com/css2?family=Open+Sans:wght@300;400;600;700&display=swap">
<style>
  :root {
    --slate: #5d6a86;
    --charcoal: #333436;
    --navy: #363853;
    --teal-veil: #3a6a86;
    --cyan: #0aa8e8;
    --blue: #1e9bd8;
    --blue-deep: #1a79b6;
    --edge-dark: #2e2f33;
    --uav-dark: #3b3e45;
    --uav-mid: #50566a;
    --white: #ffffff;
    --accent: #1aa3e0;
  }
  * { margin: 0; padding: 0; box-sizing: border-box; }
  html, body { width: 1200px; height: 848px; overflow: hidden; background: #ffffff; }
  body { font-family: "Open Sans", Arial, sans-serif; }
  .brochure { position: relative; width: 1200px; height: 848px; overflow: hidden; background: var(--slate); }

  .aerial-photo {
    position: absolute; left: 600px; top: 0; width: 600px; height: 848px;
    background:
      linear-gradient(160deg, rgba(255,255,255,0) 45%, rgba(214,238,246,0.95) 72%),
      linear-gradient(180deg, #4f7f3a 0%, #79a852 35%, #8fbf6a 55%, #b8dcc8 80%);
  }
  .uav-photo {
    position: absolute; left: 52px; top: 310px; width: 366px; height: 188px;
    border-radius: 18px;
    background: linear-gradient(160deg, var(--uav-mid) 0%, var(--uav-dark) 100%);
  }

  .services-panel {
    position: absolute; left: 0; top: 0; width: 326px; height: 246px;
    background: var(--charcoal); color: var(--white);
    padding: 44px 42px 0 42px;
  }
  .services-panel h2 { color: var(--accent); font-size: 14px; font-weight: 700; line-height: 18px; margin-bottom: 12px; }
  .services-panel p { font-size: 9.4px; line-height: 10.4px; text-align: justify; margin-bottom: 10.4px; letter-spacing: -0.1px; }

  .geometry { position: absolute; left: 0; top: 0; }

  .brand { position: absolute; left: 880px; top: 500px; display: flex; align-items: center; gap: 10px; }
  .brand-name { font-size: 40px; font-weight: 400; color: var(--accent); letter-spacing: 0.5px; }
  .brand-dot { width: 14px; height: 14px; border-radius: 50%; background: var(--accent); }

  .contact { position: absolute; right: 643px; top: 612px; text-align: right; color: var(--white); font-size: 12px; line-height: 14px; }
  .contact h3 { font-size: 12px; font-weight: 700; line-height: 14px; }
  .contact .intro { margin-bottom: 14px; }
  .contact .person { margin-bottom: 14px; }
  .contact .name { font-weight: 700; }

  .title { position: absolute; left: 641px; top: 668px; color: var(--white); font-weight: 300; font-size: 23px; line-height: 25px; }

  .web { position: absolute; left: 42px; top: 779px; color: var(--white); font-size: 12px; line-height: 15px; }
  .web strong { font-weight: 700; }
</style>
</head>
<body>
<main class="brochure">
  <div class="aerial-photo" role="img" aria-label="Aerial photograph of parkland with trees, lawn and a curving cycle path"></div>
  <div class="uav-photo" role="img" aria-label="Photograph of a quadcopter UAV in flight"></div>

  <section class="services-panel">
    <h2>Our services</h2>
    <p>As leaders in environmental science, we know how best to utilise UAV systems and technology. We have accumulated years of experience working with clients and applying knowledge to achieve sustainable results.</p>
    <p>We understand that collecting visual data, using traditional aircraft is expensive, dangerous and time consuming. Brightmoor provides a low cost, efficient solution that enables our clients to monitor, evaluate, manage and report on environmental change.</p>
  </section>

  <svg class="geometry" width="1200" height="848" viewBox="0 0 1200 848" aria-hidden="true">
    <polygon points="0,700 300,585 600,470 900,585 1200,700 1200,848 0,848" fill="var(--blue)"/>
    <polygon points="0,775 300,585 600,848 0,848" fill="var(--blue-deep)"/>
    <polygon points="1200,775 900,585 600,848 1200,848" fill="var(--blue-deep)"/>
    <polygon points="300,585 600,470 900,585 600,848" fill="var(--teal-veil)"/>
    <polygon points="600,470 850,628 600,848 350,628" fill="var(--navy)"/>
    <polygon points="0,694 300,578 300,586 0,704" fill="var(--edge-dark)"/>
    <polygon points="1200,694 900,578 900,586 1200,704" fill="var(--edge-dark)"/>
    <polygon points="300,578 600,462 900,578 900,588 600,472 300,588" fill="var(--cyan)"/>
  </svg>

  <div class="brand" aria-label="Brightmoor">
    <span class="brand-name">BRIGHTMOOR</span>
    <span class="brand-dot"></span>
  </div>

  <section class="contact">
    <h3>CONTACT US</h3>
    <p class="intro">Find out more about our services by contacting:</p>
    <div class="person">
      <p class="name">Owen Hartley</p>
      <p>Principal Scientist</p>
      <p>61 3 9000 4521</p>
      <p>Mob: 0400 512 736</p>
      <p>owen@brightmoor.com.au</p>
    </div>
    <div class="person">
      <p class="name">Marta Lindqvist</p>
      <p>Business Development Manager</p>
      <p>61 3 9000 4521</p>
      <p>Mob: 0400 287 914</p>
      <p>marta@brightmoor.com.au</p>
    </div>
  </section>

  <h1 class="title">Environmental Compliance And<br>Monitoring Services</h1>

  <p class="web">Find out more at<br><strong>www.brightmoor.com.au</strong></p>
</main>
</body>
</html>
```